Company gift Certificate

Looking for a gift certificate that would have a blank denomination. I would Like it to be 2 sided .
BrindleWorkShoppe The Way Of Casting
2475 North Alder Lane
Portsmouth RI 02948
401-586-3129
brindleworkshoppe@mailbox.example

For more info and ideas please check us out on FB and our website. I have been very happy in the past.

```html
<!DOCTYPE html>
<html lang="en">
<head>
<meta charset="utf-8">
<title>BrindleWorkShoppe Gift Certificate</title>
<link rel="stylesheet" href="https://fonts.googleapis.com/css2?family=Courgette&family=Lato:wght@400;700&family=Open+Sans:wght@800&display=swap">
<style>
  :root {
    --page-bg: #e9e6e1;
    --card-dark: #3a3c40;
    --card-mid: #5d6065;
    --photo-light: #8a8e94;
    --cork: #8a4b2c;
    --navy: #1b2f66;
    --navy-deep: #142552;
    --fish-green: #5f9a2e;
    --fish-lime: #a7c83a;
    --white: #ffffff;
    --field: #f1f1f1;
    --accent-red: #c8262c;
  }
  * { box-sizing: border-box; margin: 0; padding: 0; }
  html, body { width: 1200px; height: 750px; overflow: hidden; }
  body {
    background: var(--page-bg);
    position: relative;
    font-family: "Lato", sans-serif;
  }
  .card {
    position: absolute;
    top: 210px;
    width: 540px;
    height: 310px;
    border-radius: 4px;
    overflow: hidden;
    box-shadow: 0 6px 18px rgba(0,0,0,0.25);
  }
  /* Back side */
  .card--back {
    left: 40px;
    background: linear-gradient(180deg, var(--card-mid) 0%, var(--card-dark) 100%);
  }
  .back-photo {
    position: absolute;
    inset: 0 0 35% 0;
    background:
      linear-gradient(180deg, rgba(0,0,0,0) 55%, var(--card-mid) 100%),
      linear-gradient(100deg, var(--photo-light) 0%, #6f7378 30%, var(--cork) 45%, #6b5046 60%, #5f6368 80%, var(--photo-light) 100%);
    opacity: 0.85;
  }
  .back-title {
    position: absolute;
    top: 34px;
    left: 170px;
    width: 300px;
    font-family: "Courgette", cursive;
    font-size: 44px;
    line-height: 1.05;
    color: var(--white);
    text-align: center;
    text-shadow: 0 2px 6px rgba(0,0,0,0.35);
  }
  .back-contact {
    position: absolute;
    right: 26px;
    bottom: 46px;
    text-align: right;
    color: var(--white);
    font-weight: 700;
    font-size: 12.5px;
    line-height: 1.3;
  }
  .back-email {
    position: absolute;
    right: 26px;
    bottom: 20px;
    color: var(--white);
    font-weight: 700;
    font-size: 12px;
  }
  .brand {
    position: absolute;
    left: 30px;
    bottom: 26px;
    color: var(--white);
  }
  .brand-row { display: flex; align-items: center; gap: 8px; }
  .brand-dot {
    width: 14px; height: 14px; border-radius: 50%;
    background: var(--accent-red);
  }
  .brand-name { font-size: 20px; font-weight: 700; }
  .brand-tagline {
    margin-top: 6px;
    font-size: 9px;
    letter-spacing: 1.5px;
    font-weight: 400;
  }
  /* Front side */
  .card--front {
    left: 620px;
    background: linear-gradient(180deg, var(--navy) 0%, var(--navy-deep) 100%);
  }
  .front-photo {
    position: absolute;
    left: 60px; top: 0; right: 0; bottom: 30px;
    border-radius: 0 0 0 60% / 0 0 0 50%;
    background: radial-gradient(ellipse at 60% 45%, var(--fish-lime) 0%, var(--fish-green) 45%, rgba(40,80,60,0.6) 75%, rgba(27,47,102,0) 100%);
  }
  .front-title {
    position: absolute;
    left: 40px;
    top: 95px;
    font-family: "Open Sans", sans-serif;
    font-weight: 800;
    font-size: 44px;
    line-height: 1.05;
    color: var(--white);
    letter-spacing: 0.5px;
    text-shadow: 0 2px 4px rgba(0,0,0,0.4);
  }
  .front-hook {
    position: absolute;
    right: 80px;
    top: 40px;
  }
  .amount-field {
    position: absolute;
    right: 28px;
    bottom: 62px;
    width: 170px;
    height: 54px;
    border-radius: 16px;
    background: var(--field);
    box-shadow: 0 2px 5px rgba(0,0,0,0.3);
  }
</style>
</head>
<body>
  <section class="card card--back" aria-label="Certificate back">
    <div class="back-photo" role="img" aria-label="Close-up photo of a hand holding a fishing rod with a cork grip and reel"></div>
    <h1 class="back-title">The Way Of Casting</h1>
    <address class="back-contact">
      2475 North Alder Lane<br>
      Portsmouth RI 02948<br>
      401-586-3129
    </address>
    <div class="back-email">brindleworkshoppe@mailbox.example</div>
    <div class="brand">
      <div class="brand-row">
        <span class="brand-dot"></span>
        <span class="brand-name">BrindleWorkShoppe</span>
      </div>
      <div class="brand-tagline">CUSTOM FISHING RODS</div>
    </div>
  </section>

  <section class="card card--front" aria-label="Certificate front">
    <div class="front-photo" role="img" aria-label="Underwater photo of a large green mahi-mahi fish"></div>
    <h2 class="front-title">GIFT<br>CERTIFICATE</h2>
    <svg class="front-hook" width="60" height="150" viewBox="0 0 60 150" aria-hidden="true">
      <line x1="55" y1="0" x2="30" y2="120" stroke="#e8e8e8" stroke-width="2"/>
      <path d="M30 120 q-2 18 10 18 q10 0 8 -14" fill="none" stroke="#d8d8d8" stroke-width="3"/>
    </svg>
    <div class="amount-field" aria-label="Blank amount field"></div>
  </section>
</body>
</html>
```